Professional Website for Brightfold Laundry Company

Brightfold Laundry Company is a family-owned laundry service provider that has been serving Midtown Atlanta for over 45 years. We provide express clothing and linen washing services to residential and commercial clients in Atlanta and surrounding areas.

The final website and logo design should convey professionalism and give the customer a sense of security in having their personal items laundered with us.

Target Market(s)

Commercial Businesses and high net worth personal customers

Industry/Entity Type

Professional Laundry Services

Coding

Coded - Design and coding required

Number of Pages Required

5+ page

Font styles to use
Sans Serif

Colors
0054AA
0677BA
7BADD7
CADEEF
E8F1F8

Requirements
Must have
• I would like to have the following elements on my website: 1. Blog page 2. Contact Us Form 3. Sign up for service (sample attached) 4. Sections outlined in the content copy page 5. Links to social media accounts.
Nice to have
• A great example is https://www.quillmarsh.example/laundry-pick-up-and-delivery/?utm_term=pick%20up%20and%20delivery%20laundry%20service&utm_campaign=*QM%20United%20States%20%7C%20Search%20(Broad%20KWs)&utm_source=zorvik&utm_medium=ppc&hsa_acc=1111111111&hsa_cam=22222222222&hsa_grp=3333333333333333&hsa_ad=&hsa_src=o&hsa_tgt=kwd-44444444444444:loc-100&hsa_kw=pick%20up%20and%20delivery%20laundry%20service&hsa_mt=e&hsa_net=zorvik&hsa_ver=3&msclkid=00000000000000000000000000000000

```html
<!DOCTYPE html>
<html lang="en">
<head>
<meta charset="utf-8">
<title>Brightfold Laundry Company</title>
<link href="https://fonts.googleapis.com/css2?family=Montserrat:wght@400;500;600;700&display=swap" rel="stylesheet">
<style>
:root{
  --navy:#1f3d72;
  --navy-2:#2a4f8c;
  --blue:#0054AA;
  --blue-2:#0677BA;
  --blue-3:#7BADD7;
  --blue-4:#CADEEF;
  --blue-5:#E8F1F8;
  --orange:#F5A11F;
  --ink:#2b2b2b;
  --muted:#5a5a5a;
  --white:#ffffff;
}
*{margin:0;padding:0;box-sizing:border-box}
html,body{width:1200px;height:4093px;overflow:hidden}
body{font-family:'Montserrat',sans-serif;color:var(--ink);background:var(--white);position:relative}
.section{position:absolute;left:0;width:1200px;overflow:hidden}
.abs{position:absolute}

/* top bar */
.topbar{top:0;height:30px;background:var(--navy);color:var(--white);font-size:11px}
.topbar .item{top:8px;display:flex;align-items:center;gap:10px}
.social-dot{width:15px;height:15px;border-radius:50%;background:var(--white);top:7px}

/* header */
.header{top:30px;height:75px;background:var(--white);box-shadow:0 2px 6px rgba(0,0,0,.08);z-index:2}
.brand{display:flex;align-items:center;gap:8px;color:#1a1a1a;font-weight:600;white-space:nowrap}
.brand-dot{width:14px;height:14px;border-radius:50%;background:var(--blue-2);flex:none}
.header .brand{left:232px;top:27px;font-size:16px}
.nav{top:30px;font-size:12px;color:var(--blue)}
.btn-outline{border:2px solid var(--orange);color:var(--orange);border-radius:18px;font-size:12px;display:flex;align-items:center;justify-content:center;background:var(--white)}
.btn-solid{background:var(--orange);color:var(--white);border-radius:18px;font-size:12px;font-weight:600;display:flex;align-items:center;justify-content:center}

/* hero */
.hero{top:105px;height:559px;background:linear-gradient(160deg,#f1f6fb 0%,#dce8f5 45%,#eef4fa 60%,#d5e4f3 100%)}
.hero h1{left:230px;top:153px;font-size:27px;font-weight:600;color:var(--blue)}
.hero p{left:230px;top:200px;width:412px;font-size:14.3px;line-height:22.7px;color:var(--ink)}
.hero-photo{left:760px;top:15px;width:440px;height:535px;background:linear-gradient(180deg,#e8eef6 0%,#c97a52 30%,#b5603b 70%,#e4ebf4 100%);border-radius:40px 0 0 40px;opacity:.9}
.chat{left:1120px;top:475px;width:68px;height:68px;border-radius:50%;background:var(--orange);color:#1a1a1a;font-size:7px;display:flex;flex-direction:column;align-items:center;justify-content:center;gap:3px}
.band{top:664px;height:36px;background:var(--navy-2)}

.h2{font-size:23px;font-weight:600;color:var(--orange)}

/* services */
.services{top:700px;height:613px;background:var(--white)}
.card-label{top:115px;font-size:14px;color:#333;line-height:15px;width:200px}
.card{top:153px;width:194px;height:285px;box-shadow:6px 6px 0 var(--blue-4)}
.card.textile{background:linear-gradient(180deg,#8f6e4e,#a3835f 60%,#d6b47e)}
.card.washers{background:linear-gradient(180deg,#d9dadc,#6b6e73 40%,#c9cbcf 70%,#4a4d52)}
.card.shirts{background:linear-gradient(160deg,#5d6675,#b8c2d4 40%,#4b5566 70%,#9aa6ba)}
.card ul{list-style:none;color:var(--white);font-size:10.5px;line-height:14.4px;padding:12px 0 0 8px}
.arrow{font-size:40px;color:var(--blue-3);font-weight:300}

/* why */
.why{top:1313px;height:732px}
.why-photo{left:0;top:0;width:1200px;height:732px;background:linear-gradient(90deg,#e4edf7 0%,#d2e1f1 50%,#bcd2ec 100%)}
.why-label{font-size:12px;text-align:center;color:#1f1f1f;line-height:15px;transform:translateX(-50%);white-space:nowrap}
.why-icon{transform:translateX(-50%)}
.ring{left:435px;top:225px;width:350px;height:350px;border-radius:50%;background:var(--white);border:3px solid #3a3a3a}
.dot{width:24px;height:24px;border-radius:50%;background:#3a3a3a;transform:translate(-50%,-50%)}
.ring .brand{position:absolute;left:50%;top:50%;transform:translate(-50%,-50%);font-size:18px}

/* blog */
.blog{top:2045px;height:641px;background:var(--navy)}
.blog .desc{left:230px;top:98px;width:560px;font-size:11px;line-height:17px;color:var(--white)}
.blog-img{top:162px;width:350px;height:237px}
.blog-img.iron{left:232px;background:linear-gradient(135deg,#f2f2f2,#c9ccd1 45%,#f4f4f4 70%,#b9a48c)}
.blog-img.rack{left:618px;background:linear-gradient(180deg,#e3a64f,#c07a32 40%,#2a2a2e 75%,#18181b)}
.blog-title{top:418px;font-size:14.5px;font-weight:600;color:var(--white)}
.blog-text{top:450px;width:330px;font-size:11px;line-height:20px;color:var(--white)}
.read{top:570px;font-size:11px;color:var(--orange);display:flex;gap:12px;align-items:center}

/* testimonials + signup */
.voices{top:2686px;height:1053px;background:#e5edf6}
.quote-mark{font-size:110px;color:#c7d6e8;font-family:Georgia,serif;line-height:1}
.quote{left:372px;top:130px;width:470px;font-size:15px;line-height:26.5px;color:#2b2b2b}
.avatar{top:265px;width:50px;height:50px;transform:rotate(-10deg);border:2px solid #8a8a8a}
.pager{top:367px;left:550px;display:flex;gap:12px}
.pager span{width:11px;height:11px;border-radius:50%;background:var(--blue-4)}
.pager span.on{background:var(--blue)}
.divider{left:230px;top:430px;width:740px;height:1px;background:#b7c5d6}
.form-card{left:351px;top:532px;width:501px;height:468px;background:linear-gradient(160deg,#f1f2f2,#e3e6e8 50%,#eef0f0);box-shadow:0 4px 12px rgba(0,0,0,.15);border-radius:6px}
.form-card .lbl{font-size:11px;color:#333}
.field{height:24px;border:1px solid #7d7d7d;background:var(--white);border-radius:5px;font-size:9px;color:#9a9a9a;padding:0 7px;display:flex;align-items:center;justify-content:space-between}

/* footer */
.footer{top:3739px;height:354px;background:var(--navy);color:var(--white)}
.footer h4{font-size:13px;font-weight:600}
.footer .line{font-size:11px;font-weight:600}
.footer .small{font-size:9px}
.f-social{width:28px;height:28px;border-radius:50%;border:2px solid var(--white);background:var(--white)}
.f-input{border-bottom:1px solid var(--white);font-size:8.5px;color:#b9c6dc;padding-bottom:3px}
.f-area{border:1px solid #b9c6dc;font-size:8.5px;color:#b9c6dc;padding:4px 6px}
.f-links{display:flex;gap:18px;font-size:9px;font-weight:600}
</style>
</head>
<body>

<div class="section topbar">
  <div class="abs item" style="left:232px">
    <svg width="12" height="12" viewBox="0 0 24 24"><path fill="#fff" d="M6.6 10.8a15.1 15.1 0 0 0 6.6 6.6l2.2-2.2c.3-.3.7-.4 1-.2 1.1.4 2.3.6 3.6.6.6 0 1 .4 1 1V20c0 .6-.4 1-1 1A17 17 0 0 1 3 4c0-.6.4-1 1-1h3.5c.6 0 1 .4 1 1 0 1.3.2 2.5.6 3.6.1.3 0 .7-.2 1z"/></svg>
    <span>404-555-0142</span>
  </div>
  <div class="abs item" style="left:374px">
    <svg width="16" height="12" viewBox="0 0 16 12"><rect x="0.5" y="0.5" width="15" height="11" fill="none" stroke="#fff"/><path d="M.5.5 8 7l7.5-6.5" fill="none" stroke="#fff"/></svg>
    <span>info@brightfoldlaundry.com</span>
  </div>
  <div class="abs social-dot" style="left:880px"></div>
  <div class="abs social-dot" style="left:905px"></div>
  <div class="abs social-dot" style="left:930px"></div>
  <div class="abs social-dot" style="left:955px"></div>
</div>

<header class="section header">
  <div class="abs brand"><span class="brand-dot"></span>Brightfold Laundry Company</div>
  <nav>
    <span class="abs nav" style="left:520px">Services &#8964;</span>
    <span class="abs nav" style="left:598px">About Us</span>
    <span class="abs nav" style="left:683px">FAQs</span>
    <span class="abs nav" style="left:745px">Blog</span>
    <span class="abs nav" style="left:804px">Login</span>
  </nav>
  <div class="abs btn-outline" style="left:858px;top:21px;width:114px;height:33px">Sign Up Now</div>
</header>

<section class="section hero">
  <h1 class="abs">Clean is our middle name!</h1>
  <p class="abs">Brightfold Laundry Company is a family-owned laundry service provider that has been serving Midtown Atlanta for over 45 years. We are proud to offer high quality and convenient services to the area residents and business owners and strive to keep our customers' clothing in tip top shape.</p>
  <div class="abs btn-solid" style="left:230px;top:385px;width:135px;height:34px">Sign Up Now</div>
  <div class="abs hero-photo" role="img" aria-label="Photo of a hand holding a rust-coloured jacket on a hanger"></div>
  <div class="abs chat">
    <svg width="24" height="22" viewBox="0 0 24 22"><circle cx="12" cy="7" r="5" fill="#1a1a1a"/><path d="M2 22c0-6 4.5-9 10-9s10 3 10 9z" fill="#1a1a1a"/></svg>
    <span>Chat With Us</span>
  </div>
</section>

<div class="section band">
  <svg class="abs" style="left:585px;top:8px" width="30" height="20" viewBox="0 0 30 20"><path d="M3 4l12 11L27 4" fill="none" stroke="#fff" stroke-width="3.5"/></svg>
</div>

<section class="section services">
  <svg class="abs" style="left:0;top:0" width="1200" height="613">
    <polygon points="50,0 100,0 80,55 58,55" fill="#CADEEF"/>
    <polygon points="100,0 145,0 120,45 95,45" fill="#b9c8dc"/>
    <polygon points="1010,40 1035,40 1060,110 1030,110" fill="#b9c8dc"/>
    <polygon points="1045,0 1110,0 1180,160 1120,160" fill="#b9c8dc"/>
    <polygon points="1140,0 1200,0 1200,110 1185,110" fill="#CADEEF"/>
    <polygon points="0,470 40,470 80,613 30,613" fill="#b9c8dc"/>
    <polygon points="45,520 80,520 120,613 75,613" fill="#b9c8dc"/>
    <polygon points="1120,560 1135,560 1145,613 1125,613" fill="#b9c8dc"/>
    <polygon points="1150,510 1185,510 1200,613 1165,613" fill="#b9c8dc"/>
    <polygon points="1150,430 1200,430 1200,470 1165,470" fill="#CADEEF"/>
  </svg>
  <h2 class="abs h2" style="left:230px;top:46px">Services</h2>
  <div class="abs arrow" style="left:228px;top:250px">&#10216;</div>
  <div class="abs arrow" style="left:950px;top:250px">&#10217;</div>

  <div class="abs card-label" style="left:268px;top:116px">Commercial Services</div>
  <div class="abs card textile" style="left:268px" role="img" aria-label="Close-up photo of folded textiles">
    <ul>
      <li>What we launder:</li>
      <li>• Linens</li><li>• Sheets</li><li>• Pillow cases</li><li>• Table cloths</li><li>• Towels</li>
      <li>• Comforters &amp; bedspreads</li><li>• Blankets &amp; pillows</li><li>• Duvet covers</li>
      <li>• Mattress covers</li><li>• Uniforms</li><li>• Scrubs</li><li>• Reusable PPE</li>
      <li>• Curtains &amp; drapes</li><li>• Custom-owned goods &amp; more.</li>
    </ul>
  </div>

  <div class="abs card-label" style="left:505px">Light Commercial<br>Services</div>
  <div class="abs card washers" style="left:505px" role="img" aria-label="Photo of stacked commercial washing machines"></div>

  <div class="abs card-label" style="left:738px">Professional Laundry<br>Services</div>
  <div class="abs card shirts" style="left:740px" role="img" aria-label="Photo of pressed shirts and jackets on hangers"></div>

  <div class="abs btn-outline" style="left:532px;top:511px;width:135px;height:34px">Sign Up Now</div>
</section>

<section class="section why">
  <div class="abs why-photo" role="img" aria-label="Faded photo of a row of laundromat washing machines"></div>
  <svg class="abs" style="left:0;top:0" width="1200" height="732"><polygon points="1015,0 1200,0 1200,732 1165,732" fill="#2a5aa0" opacity=".85"/></svg>
  <h2 class="abs h2" style="left:232px;top:60px">Why Choose Us</h2>

  <div class="abs ring">
    <div class="brand"><span class="brand-dot"></span>Brightfold Laundry Company</div>
  </div>
  <div class="abs dot" style="left:610px;top:225px"></div>
  <div class="abs dot" style="left:741px;top:287px"></div>
  <div class="abs dot" style="left:783px;top:403px"></div>
  <div class="abs dot" style="left:721px;top:533px"></div>
  <div class="abs dot" style="left:499px;top:533px"></div>
  <div class="abs dot" style="left:434px;top:405px"></div>
  <div class="abs dot" style="left:475px;top:284px"></div>

  <svg class="abs why-icon" style="left:610px;top:127px" width="34" height="40" viewBox="0 0 34 40"><path d="M4 2h26M4 38h26M7 2c0 12 20 12 20 18S7 26 7 38M27 2c0 12-20 12-20 18s20 6 20 18" fill="none" stroke="#1a1a1a" stroke-width="3"/><path d="M11 34l6-6 6 6z" fill="#1a1a1a"/></svg>
  <div class="abs why-label" style="left:610px;top:174px">We Help You Optimize Your Time</div>

  <svg class="abs why-icon" style="left:368px;top:231px" width="48" height="48" viewBox="0 0 48 48" fill="none" stroke="#1a1a1a" stroke-width="2"><circle cx="24" cy="13" r="10"/><path d="M6 20v14l10 12M42 20v14L32 46M12 24l6 10M36 24l-6 10"/></svg>
  <div class="abs why-label" style="left:364px;top:290px">We Have Knowledgeable,<br>Friendly Team Members</div>

  <svg class="abs why-icon" style="left:858px;top:220px" width="44" height="54" viewBox="0 0 44 54" fill="none" stroke="#1a1a1a" stroke-width="2"><rect x="2" y="2" width="40" height="50" rx="3"/><path d="M2 12h40"/><circle cx="8" cy="7" r="2"/><circle cx="22" cy="32" r="13"/><circle cx="22" cy="32" r="8"/></svg>
  <div class="abs why-label" style="left:852px;top:288px">We Utilize Modern,<br>Industrial-size Washer<br>&amp; Dryer Equipment</div>

  <svg class="abs why-icon" style="left:312px;top:375px" width="58" height="52" viewBox="0 0 58 52" fill="none" stroke="#1a1a1a" stroke-width="2"><rect x="19" y="2" width="20" height="8"/><path d="M4 14h50v6H4zM6 20v30h46V20M12 26h34v8H12zM14 40h10v10H14zM32 40h14v6H32"/></svg>
  <div class="abs why-label" style="left:312px;top:434px">Our Facility is Bright,<br>Clean and Comfortable</div>

  <svg class="abs why-icon" style="left:893px;top:379px" width="54" height="50" viewBox="0 0 54 50" fill="none" stroke="#1a1a1a" stroke-width="2"><circle cx="10" cy="10" r="7"/><circle cx="10" cy="10" r="3"/><rect x="24" y="4" width="26" height="12"/><rect x="24" y="22" width="26" height="10"/><rect x="24" y="38" width="26" height="10"/><path d="M17 10h7M10 17v26h14M10 27h14"/></svg>
  <div class="abs why-label" style="left:895px;top:440px">We Provide Custimized<br>Business Solutions</div>

  <svg class="abs why-icon" style="left:413px;top:540px" width="46" height="52" viewBox="0 0 46 52" fill="none" stroke="#1a1a1a" stroke-width="2"><path d="M4 14h30v30H4zM8 14l14-10 8 10M30 6l8 4"/><circle cx="30" cy="38" r="10"/><path d="M30 32v12M27 35h5a2 2 0 0 1 0 4h-4a2 2 0 0 0 0 4h5"/></svg>
  <div class="abs why-label" style="left:407px;top:604px">We Provide Payment Options</div>

  <svg class="abs why-icon" style="left:806px;top:540px" width="32" height="46" viewBox="0 0 32 46" fill="none" stroke="#1a1a1a" stroke-width="2.5"><path d="M16 42S3 26 3 16a13 13 0 0 1 26 0c0 10-13 26-13 26z"/><circle cx="16" cy="16" r="5"/><path d="M6 44h20"/></svg>
  <div class="abs why-label" style="left:806px;top:600px">Convenient Location</div>
</section>

<section class="section blog">
  <svg class="abs" style="left:0;top:0" width="1200" height="641">
    <polygon points="0,0 230,0 60,641 0,641" fill="#27498a"/>
    <polygon points="840,0 1200,0 1200,641 1100,641" fill="#23437c"/>
  </svg>
  <h2 class="abs h2" style="left:230px;top:56px">Latest Blog Posts</h2>
  <div class="abs read" style="left:888px;top:74px">Visit Blog <span style="color:var(--white)">&#8250;</span></div>
  <p class="abs desc">Quo tenetur deserunt non similique dolorem aut consequatur aperiam et similique laboriosam sit harum dolores. Et assumenda provident nam modi tenetur et obcaecati iure.</p>
  <div class="abs arrow" style="left:183px;top:255px;color:var(--blue-4)">&#10216;</div>
  <div class="abs arrow" style="left:993px;top:255px;color:var(--blue-4)">&#10217;</div>

  <div class="abs blog-img iron" role="img" aria-label="Photo of hands ironing a white shirt"></div>
  <div class="abs blog-title" style="left:232px">Tips and Tricks for best ironing practices</div>
  <p class="abs blog-text" style="left:232px">Lorem ipsum dolor sit amet, consectetur adipisicing elit, sed do eiusmod tempor incididunt ut labore et dolore magna aliqua. sed qudol magnam aliquam quaerat voluptatem.</p>
  <div class="abs read" style="left:232px">Read more <span style="color:var(--orange)">&#8250;</span></div>

  <div class="abs blog-img rack" role="img" aria-label="Photo of garments on wooden hangers"></div>
  <div class="abs blog-title" style="left:618px">Optimizing your wardrobe space</div>
  <p class="abs blog-text" style="left:618px;line-height:17px">Quo tenetur deserunt non similique dolorem aut consequatur aperiam et similique laboriosam sit harum dolores. Et assumenda provident nam modi tenetur et obcaecati iure.</p>
  <div class="abs read" style="left:618px">Read more <span style="color:var(--orange)">&#8250;</span></div>
</section>

<section class="section voices">
  <svg class="abs" style="left:0;top:0" width="1200" height="1053">
    <polygon points="700,0 1010,0 1200,620 1200,1053 980,1053 840,450" fill="#edf3f9"/>
    <polygon points="0,0 180,0 0,400" fill="#dfe8f3"/>
  </svg>
  <h2 class="abs h2" style="left:230px;top:38px">Hear what our customers say about us</h2>
  <div class="abs quote-mark" style="left:292px;top:90px">&#8220;</div>
  <div class="abs quote-mark" style="left:848px;top:200px">&#8221;</div>
  <p class="abs quote">A very convenient &amp; professional service! We've been using Brightfold Laundry Company for years now. The pick-up services is also quite convenient for us especially with email and text notification. The prices also make it very affordable!</p>
  <div class="abs avatar" style="left:383px;background:#c9c2bb" role="img" aria-label="Customer portrait"></div>
  <div class="abs avatar" style="left:576px;background:var(--orange);border-color:#6a6a6a" role="img" aria-label="Customer portrait"></div>
  <div class="abs avatar" style="left:775px;background:#cfd3d6" role="img" aria-label="Customer portrait"></div>
  <div class="abs" style="left:576px;top:324px;font-size:10px;color:#333">Marcus Dell</div>
  <div class="abs pager"><span></span><span class="on"></span><span></span><span></span><span></span></div>
  <div class="abs divider"></div>
  <h2 class="abs h2" style="left:0;width:1200px;text-align:center;top:466px">Sign Up Today!</h2>

  <div class="abs form-card">
    <div class="abs" style="left:18px;top:28px;font-size:15px;font-weight:600;color:#333">LET'S GET STARTED</div>
    <div class="abs" style="left:18px;top:54px;font-size:10.5px;color:#444">Complete the form below to schedule a pick up or delivery.</div>
    <div class="abs lbl" style="left:18px;top:92px">What's your Zip Code?</div>
    <div class="abs field" style="left:18px;top:116px;width:79px">Zip Code</div>
    <div class="abs lbl" style="left:18px;top:173px">Name *</div>
    <div class="abs field" style="left:18px;top:195px;width:163px">First name</div>
    <div class="abs field" style="left:211px;top:195px;width:163px">Last name</div>
    <div class="abs lbl" style="left:18px;top:257px">Email *</div>
    <div class="abs field" style="left:18px;top:278px;width:163px"></div>
    <div class="abs lbl" style="left:211px;top:257px">Phone *</div>
    <div class="abs field" style="left:211px;top:278px;width:163px"></div>
    <div class="abs lbl" style="left:18px;top:338px">Best time to reach you? *</div>
    <div class="abs field" style="left:18px;top:360px;width:163px;color:#333">Morning (7- 12 am) <span>&#8964;</span></div>
    <div class="abs lbl" style="left:211px;top:338px">How can we help? *</div>
    <div class="abs field" style="left:211px;top:360px;width:163px;color:#333">Need to schedule pick up <span>&#8964;</span></div>
    <div class="abs btn-solid" style="left:211px;top:418px;width:77px;height:25px;border-radius:6px;font-weight:500;font-size:11px">Next</div>
  </div>
</section>

<footer class="section footer">
  <h4 class="abs" style="left:230px;top:36px">Contact Us</h4>
  <div class="abs line" style="left:230px;top:73px">info@brightfoldlaundry.com</div>
  <div class="abs line" style="left:230px;top:100px">404-555-0142</div>
  <div class="abs line" style="left:230px;top:161px">Follow us on social media</div>
  <div class="abs f-social" style="left:231px;top:202px"></div>
  <div class="abs f-social" style="left:278px;top:202px"></div>
  <div class="abs f-social" style="left:324px;top:202px"></div>
  <div class="abs f-social" style="left:372px;top:202px"></div>

  <h4 class="abs" style="left:469px;top:36px">Our services</h4>
  <div class="abs line" style="left:469px;top:72px;font-size:10px;line-height:20px">Wash &amp; Fold<br>Dry Cleaning<br>Commercial Laundry<br>Pick up &amp; Delivery</div>

  <h4 class="abs" style="left:717px;top:36px">Have a question for us?</h4>
  <div class="abs small" style="left:717px;top:74px">Fill out the form below and send us an email</div>
  <div class="abs f-input" style="left:717px;top:108px;width:116px">First name *</div>
  <div class="abs f-input" style="left:847px;top:108px;width:116px">Last name</div>
  <div class="abs f-input" style="left:717px;top:141px;width:116px">Email address *</div>
  <div class="abs f-area" style="left:717px;top:170px;width:246px;height:51px">Type your query here</div>
  <div class="abs btn-outline" style="left:717px;top:234px;width:113px;height:27px;background:transparent;font-size:10px;color:var(--white)">Send</div>

  <div class="abs" style="left:230px;top:278px;width:740px;height:1px;background:#7d93b8"></div>
  <div class="abs small" style="left:230px;top:310px">© Copyright 2022 brightfoldlaundry.com</div>
  <div class="abs f-links" style="left:708px;top:310px"><span>Privacy</span><span>Terms &amp; Conditions</span><span>Cookie Policy</span><span>Sitemap</span></div>
  <svg class="abs" style="left:1165px;top:325px" width="26" height="16" viewBox="0 0 26 16"><path d="M2 14L13 3l11 11" fill="none" stroke="#CADEEF" stroke-width="3.5"/></svg>
</footer>

</body>
</html>
```